"Pause. Pivot. Prosper." Empowerment Book Cover

Hello, I need a hot, trendy, and contemporary book cover designed for my first book called "Pause. Pivot. Prosper. -- 365 Bold Confidence Notes for Anyone Seeking to Pause, Pivot, and Prosper Across Career & Personal Dreams."
This is my first book and I am really wanting to launch my brand with it... it would be awesome to match the inside/outside branding of the book. So we can either create the book cover to match the book guts, or update the book guts to match the cover.
Lastly, I just got a professional photoshoot done last week so we can use one of those images, or we can go with a different idea/style for the cover. The body of the book is attached. All questions welcomed, happy designing!
Target Market(s)
Gen Z, Millennials and Gen X.
Industry/Entity Type
Personal Development.
Requirements
Must have
- It must stand out and be different from other typical book covers.
Nice to have
- Success, Inspiration, Motivation, Mindset, Growth.
Should not have
- Clipart, stock art, stock look and feel.

```html
<!DOCTYPE html>
<html lang="en">
<head>
<meta charset="utf-8">
<title>Pause. Pivot. Prosper. — Book Cover</title>
<link rel="stylesheet" href="https://fonts.googleapis.com/css2?family=Jost:wght@500;600;700;800&display=swap">
<style>
  :root {
    --canvas-bg: #f5f5f4;
    --cover-dark: #262626;
    --cover-mid: #2f2f2f;
    --copper: #c47a38;
    --copper-light: #d69452;
    --gold-dark: #8f5e2a;
    --gold-light: #e0a862;
    --white: #f7f7f5;
    --author: #c8742f;
  }
  * { margin: 0; padding: 0; box-sizing: border-box; }
  html, body {
    width: 1200px; height: 1200px; overflow: hidden;
    background: var(--canvas-bg);
    font-family: "Jost", "Futura", sans-serif;
  }
  .book-cover {
    position: absolute;
    left: 226px; top: 40px;
    width: 747px; height: 1120px;
    background: radial-gradient(ellipse at 50% 35%, var(--cover-mid), var(--cover-dark) 75%);
    overflow: hidden;
  }
  .paper-opening {
    position: absolute; left: 0; top: 0;
    width: 747px; height: 640px;
  }
  .teaser {
    position: absolute; left: 0; width: 747px;
    text-align: center; color: var(--white);
    font-weight: 700; text-transform: uppercase;
    line-height: 1;
  }
  .teaser-line { position: absolute; left: 0; right: 0; transform: translateX(13px); }
  .teaser-number { top: 206px; font-size: 118px; font-weight: 800; letter-spacing: -2px; }
  .teaser-bold   { top: 318px; font-size: 44px; font-weight: 600; }
  .teaser-conf   { top: 370px; font-size: 30px; font-weight: 600; letter-spacing: -0.5px; }
  .teaser-for    { top: 410px; font-size: 40px; font-weight: 600; }
  .teaser-seek   { top: 460px; font-size: 30px; font-weight: 600; }

  .title {
    position: absolute; left: 0; width: 747px;
    text-align: center; text-transform: uppercase;
    font-weight: 800; line-height: 1;
  }
  .title-word {
    position: absolute; left: 0; right: 0;
    font-size: 122px; letter-spacing: -1px;
    background: linear-gradient(90deg, var(--gold-dark), var(--gold-light) 30%, var(--copper) 55%, var(--gold-dark) 70%, var(--gold-light));
    -webkit-background-clip: text; background-clip: text;
    color: transparent;
    text-shadow: 0 4px 8px rgba(0,0,0,0.25);
  }
  .title-pause   { top: 620px; }
  .title-pivot   { top: 738px; }
  .title-prosper { top: 856px; }

  .subtitle {
    position: absolute; left: 0; right: 0; top: 983px;
    text-align: center; color: var(--white);
    font-size: 25px; font-weight: 700; letter-spacing: 3.5px;
    text-transform: uppercase;
  }
  .author {
    position: absolute; left: 0; right: 0; top: 1050px;
    text-align: center; color: var(--author);
    font-size: 46px; font-weight: 600; letter-spacing: 9px;
    text-transform: uppercase;
  }
</style>
</head>
<body>
  <main class="book-cover">
    <svg class="paper-opening" viewBox="0 0 747 640" role="img" aria-label="Torn paper opening with curled dark edges revealing a copper layer">
      <defs>
        <linearGradient id="copperFill" x1="0" y1="0" x2="1" y2="1">
          <stop offset="0" stop-color="#b86f30"/>
          <stop offset="0.5" stop-color="#c98540"/>
          <stop offset="1" stop-color="#b06a2e"/>
        </linearGradient>
      </defs>
      <polygon points="372,20 580,190 700,334 520,510 380,640 230,510 75,334 210,190" fill="#1f1f1f"/>
      <polygon points="372,70 633,334 379,585 146,334" fill="url(#copperFill)"/>
    </svg>

    <div class="teaser">
      <div class="teaser-line teaser-number">365</div>
      <div class="teaser-line teaser-bold">Bold</div>
      <div class="teaser-line teaser-conf">Confidence Notes</div>
      <div class="teaser-line teaser-for">For Anyone</div>
      <div class="teaser-line teaser-seek">Seeking To</div>
    </div>

    <h1 class="title">
      <span class="title-word title-pause">Pause</span>
      <span class="title-word title-pivot">Pivot</span>
      <span class="title-word title-prosper">Prosper</span>
    </h1>

    <p class="subtitle">Across Career &amp; Personal Dreams.</p>
    <p class="author">Samir Okafor</p>
  </main>
</body>
</html>
```